Fundraising team needing letterhead for sponsorship and donations

I would like a design that relates to our team name Rosy Spoke Riders. We ride in an annual bicycle event that raises money that goes towards cancer research.We already have a team jersey designed which i have attached. The team name we would prefer to be in pink. Our team includes males and females. The logo also needs to relate to bike riding.

Industry/Entity Type

Event

Font styles to use
Sans Serif

```html
<!DOCTYPE html>
<html lang="en">
<head>
<meta charset="utf-8">
<title>Rosy Spoke Riders — Letterhead</title>
<link rel="stylesheet" href="https://fonts.googleapis.com/css2?family=Open+Sans:wght@400;600&family=Satisfy&display=swap">
<style>
  :root {
    --backdrop: #f4f4f4;
    --paper: #ffffff;
    --ink: #4a4a4a;
    --ink-soft: #6b6b6b;
    --rose: #d81b7a;
    --rose-faint: #fbe3ec;
    --band-deep: #c41e5a;
    --band-mid: #e8407c;
    --band-light: #f29bbd;
  }
  * { box-sizing: border-box; margin: 0; padding: 0; }
  html, body {
    width: 1200px; height: 1000px; overflow: hidden;
    background: var(--backdrop);
    font-family: "Open Sans", Arial, sans-serif;
  }
  .letterhead {
    position: absolute; left: 264px; top: 30px;
    width: 672px; height: 940px;
    background: var(--paper);
    box-shadow: 0 4px 18px rgba(0,0,0,0.15);
    overflow: hidden;
  }
  .sender {
    position: absolute; left: 46px; top: 44px; color: var(--ink);
  }
  .sender-tagline {
    font-family: "Satisfy", cursive;
    font-size: 14px; color: var(--ink); margin-bottom: 5px;
  }
  .sender-address {
    font-size: 7.5px; line-height: 10px; color: var(--ink-soft);
  }
  .sender-contacts {
    display: flex; gap: 18px; margin-top: 8px;
    font-size: 7.5px; color: var(--ink-soft);
  }
  .contact { display: flex; align-items: center; gap: 4px; }
  .contact svg { width: 10px; height: 10px; }
  .brand {
    position: absolute; right: 34px; top: 128px;
    display: flex; align-items: center; gap: 8px;
  }
  .brand-dot {
    width: 14px; height: 14px; border-radius: 50%; background: var(--rose);
  }
  .brand-name {
    font-size: 21px; font-weight: 600; color: var(--rose);
    letter-spacing: 0.5px;
  }
  .watermark {
    position: absolute; left: 0; right: 0; top: 440px;
    text-align: center;
    font-size: 44px; font-weight: 600; color: var(--rose-faint);
  }
  .footer-band {
    position: absolute; left: 0; bottom: 0; width: 672px; height: 80px;
    background: linear-gradient(180deg, var(--band-deep) 0%, var(--band-mid) 45%, var(--band-light) 100%);
  }
</style>
</head>
<body>
  <main class="letterhead">
    <header class="sender">
      <p class="sender-tagline">Fundraising Bike Ride for Cancer Research</p>
      <p class="sender-address">Organized by:<br>Name of the organization , address Line 1, Address Line 2 and<br>City</p>
      <div class="sender-contacts">
        <span class="contact">
          <svg viewBox="0 0 10 10"><circle cx="5" cy="5" r="4.4" fill="none" stroke="#6b6b6b" stroke-width="0.8"/><path d="M3.4 2.8l1 1-0.5 0.7c0.3 0.7 0.8 1.2 1.5 1.5l0.7-0.5 1 1-0.7 0.8C4.8 7.1 2.9 5.2 2.7 3.5z" fill="#6b6b6b"/></svg>
          0400 555 018
        </span>
        <span class="contact">
          <svg viewBox="0 0 10 10"><rect x="0.6" y="1.6" width="8.8" height="6.8" rx="1" fill="none" stroke="#6b6b6b" stroke-width="0.8"/><circle cx="5" cy="5" r="2" fill="none" stroke="#6b6b6b" stroke-width="0.6"/><path d="M3 5h4M5 3v4" stroke="#6b6b6b" stroke-width="0.5"/></svg>
          www.rosyspokeriders.org.au
        </span>
        <span class="contact">
          <svg viewBox="0 0 10 10"><circle cx="5" cy="5" r="4.4" fill="none" stroke="#6b6b6b" stroke-width="0.8"/><circle cx="5" cy="5" r="1.5" fill="none" stroke="#6b6b6b" stroke-width="0.8"/></svg>
          info@rosyspokeriders.org.au
        </span>
      </div>
    </header>

    <div class="brand">
      <span class="brand-dot"></span>
      <span class="brand-name">Rosy Spoke Riders</span>
    </div>

    <div class="watermark">Rosy Spoke Riders</div>

    <div class="footer-band" role="img" aria-label="Decorative pink wave band along the foot of the page"></div>
  </main>
</body>
</html>
```